TK AG Flyer design

I’d like to redesign an A5, double-sided flyer for the company TK AG (www.tkag.lu). The text/content is available in a Word document.

```html
<!DOCTYPE html>
<html lang="de">
<head>
<meta charset="utf-8">
<title>TK AG Luzern – Flyer A5</title>
<link rel="stylesheet" href="https://fonts.googleapis.com/css2?family=Arimo:wght@400;700&display=swap">
<style>
  :root{
    --navy:#2b2e85;
    --orange:#e9ab3c;
    --cream:#fbecd2;
    --paper:#ffffff;
    --stage:#000000;
  }
  *{box-sizing:border-box;margin:0;padding:0}
  html,body{width:1200px;height:862px;overflow:hidden;background:var(--stage)}
  body{position:relative;font-family:"Arimo",Arial,sans-serif;color:var(--navy)}
  .page{position:absolute;top:45px;width:538px;height:764px;background:var(--paper);overflow:hidden}
  .page--front{left:50px}
  .page--back{left:613px}
  .hero{position:absolute;left:0;top:0;width:100%;height:147px}
  .hero--worker{background:linear-gradient(160deg,#b9d4ef 0%,#8fb3df 35%,#2d4f9c 60%,#1e3570 100%)}
  .hero--roof{background:linear-gradient(200deg,#2c3f78 0%,#3f5fa8 45%,#a9b7cf 75%,#8a6c54 100%)}
  .abs{position:absolute}
  .headline{font-weight:700;font-size:22.5px;line-height:27.5px}
  .headline span{background:linear-gradient(transparent 45%,var(--orange) 45%,var(--orange) 92%,transparent 92%);padding:0 1px}
  .body{font-size:13.3px;line-height:18.4px}
  .body b{font-weight:700}
  .section-title{font-size:21px;font-weight:400;display:flex;align-items:center;gap:5px;line-height:24px}
  .sub{font-size:13.3px;font-weight:700;line-height:18px}
  .list{list-style:none;font-size:13.3px;line-height:18.1px}
  .list li{position:relative;padding-left:29px}
  .list li::before{content:"";position:absolute;left:15px;top:7px;width:5px;height:5px;border-radius:50%;background:var(--navy)}
  .brand{display:flex;align-items:center;gap:12px;font-weight:700;white-space:nowrap}
  .brand__mark{background:var(--navy)}
  .badge{position:absolute;left:354px;top:586px;width:154px;height:154px;border-radius:50%;background:var(--orange);
    display:flex;flex-direction:column;align-items:center;justify-content:center;transform:rotate(-12deg);text-align:center}
  .badge__lead{font-weight:700;font-size:13.5px;line-height:16px}
  .badge__phone{font-weight:700;font-size:23px;margin-top:4px}
  .badge__mail{font-size:13px;margin-top:3px}
  .option{display:flex;gap:9px;font-size:13.3px;line-height:16.2px}
  .option svg{flex:none}
  .h3{font-size:15.5px;font-weight:700;line-height:18px;white-space:nowrap}
  .para{font-size:13.3px;line-height:16.1px;white-space:nowrap}
  .steps{position:absolute;left:37px;top:514px;width:464px;height:123px;border-radius:15px;
    background:linear-gradient(90deg,var(--orange) 0%,#f0c57a 50%,var(--cream) 100%);padding:13px 14px}
  .steps__title{font-size:13.3px;font-weight:700;line-height:16px}
  .steps ol{list-style:none;font-size:13.3px;line-height:16.1px;padding-left:14px;margin-top:1px}
  .steps ol b{font-weight:700}
  .footer{font-size:11.6px;line-height:14px;white-space:nowrap}
</style>
</head>
<body>

<section class="page page--front">
  <div class="hero hero--worker" role="img" aria-label="Foto: Monteur mit Schutzhelm auf einem Dach mit Solarmodulen"></div>

  <h1 class="abs headline" style="left:34px;top:158px">
    <span>Mehr Eigenverbrauch.</span><br><span>Mehr Effizienz.</span><br><span>Mehr Zukunft.</span>
  </h1>
  <p class="abs body" style="left:34px;top:241px;width:440px">Wir planen und beraten rund um Photovoltaik und Energieeffizienz –<br>für <b>Private, Gewerbe und Industrie.</b></p>

  <h2 class="abs section-title" style="left:34px;top:304px">
    <svg width="24" height="22" viewBox="0 0 24 22" aria-hidden="true"><circle cx="6" cy="5" r="4" fill="var(--orange)"/><rect x="2" y="4" width="20" height="14" fill="none" stroke="var(--navy)" stroke-width="1.4"/><path d="M2 9h20M2 13.5h20M7 4v14M12 4v14M17 4v14M9 18l-2 3h10l-2-3" fill="none" stroke="var(--navy)" stroke-width="1.2"/></svg>
    Solar Energie
  </h2>
  <p class="abs sub" style="left:34px;top:336px">Photovoltaik-Lösungen, die zu Ihrem Dach passen</p>
  <ul class="abs list" style="left:34px;top:354px;width:400px">
    <li><b>Indach PV-Anlagen</b> (integriert &amp; ästhetisch)</li>
    <li><b>Aufdach PV-Anlagen</b> (effizient &amp; preis-/leistungsstark)</li>
    <li><b>Eigenverbrauch optimieren</b> (Batterie, Wärmepumpe,<br>E-Mobility, smartes Lastmanagement)</li>
  </ul>

  <h2 class="abs section-title" style="left:34px;top:444px">
    <svg width="24" height="26" viewBox="0 0 24 26" aria-hidden="true"><path d="M7 8a8 8 0 1 0 10 0" fill="none" stroke="var(--navy)" stroke-width="3.2" stroke-linecap="round"/><path d="M13 1l-3 7h3l-2 6" fill="none" stroke="var(--orange)" stroke-width="1.8"/></svg>
    Energie Effizienz
  </h2>
  <p class="abs sub" style="left:34px;top:476px">Beratung &amp; Konzepte für nachhaltige Gebäude</p>
  <ul class="abs list" style="left:34px;top:494px;width:400px">
    <li><b>Energieberatung / GEAK / GEAK Plus</b></li>
    <li><b>Impulsberatung &amp; Energiekonzept</b> (HLK + PV,<br>Simulationen, Nachweise)</li>
    <li><b>Energiesanierung</b> (Planung, Koordination,<br>Förderabwicklung)</li>
  </ul>

  <div class="abs brand" style="left:40px;top:652px;font-size:33px">
    <span class="brand__mark" style="width:52px;height:52px"></span>TK AG Luzern
  </div>

  <div class="badge">
    <span class="badge__lead">Jetzt unverbindlich<br>Kontakt aufnehmen</span>
    <span class="badge__phone">XX XXX XX</span>
    <span class="badge__mail">kontakt@tkag.lu</span>
  </div>
</section>

<section class="page page--back">
  <div class="hero hero--roof" role="img" aria-label="Foto: Schrägdach mit Solarmodulen und Kamin"></div>

  <h1 class="abs headline" style="left:37px;top:158px">
    <span>Indach oder Aufdach?</span><br><span>Wir finden die passende Lösung.</span>
  </h1>

  <div class="abs option" style="left:37px;top:219px;width:470px">
    <svg width="28" height="30" viewBox="0 0 28 30" aria-hidden="true"><circle cx="14" cy="5" r="3" fill="none" stroke="var(--orange)" stroke-width="1.2"/><rect x="1" y="14" width="26" height="14" fill="none" stroke="var(--navy)" stroke-width="1.4"/><path d="M1 19h26M1 23.5h26M7.5 14v14M14 14v14M20.5 14v14" stroke="var(--navy)" stroke-width="1.2"/></svg>
    <p><b>Indach PV</b> ist ideal bei Neubau oder Dachsanierung: Module ersetzen die Dacheindeckung – funktional und optisch hochwertig.</p>
  </div>
  <div class="abs option" style="left:37px;top:268px;width:470px">
    <svg width="28" height="30" viewBox="0 0 28 30" aria-hidden="true"><circle cx="4" cy="4" r="2.5" fill="none" stroke="var(--orange)" stroke-width="1.2"/><path d="M7 10h14l-5 18H2z M21 10l6 18h-11" fill="none" stroke="var(--navy)" stroke-width="1.4"/><path d="M4 17h15M3 22.5h14M12 10l-5 18M17 10l-5 18" stroke="var(--navy)" stroke-width="1.1"/></svg>
    <p><b>Aufdach PV</b> eignet sich besonders bei bestehenden Dächern in gutem Zustand – mit Standardmodulen oft die effizienteste Technologie zum besten Preis.</p>
  </div>

  <h3 class="abs h3" style="left:37px;top:335px">Eigenverbrauch erhöhen – Rendite steigern</h3>
  <p class="abs para" style="left:37px;top:355px">Viele PV-Anlagen produzieren mehr Strom, als gleichzeitig benötigt wird.<br>Mit passenden Massnahmen erhöhen Sie Ihren Eigenverbrauch – z. B.<br>durch <b>Batteriesysteme, Wärmepumpen-Ansteuerung, überschussvariables<br>Laden von E-Fahrzeugen</b> oder gezieltes Schalten von Verbrauchern.</p>

  <h3 class="abs h3" style="left:37px;top:429px">Energieberatung &amp; Sanierung – ganzheitlich gedacht</h3>
  <p class="abs para" style="left:37px;top:449px">Wir analysieren Ihr Gebäude, erstellen einen <b>Sanierungs- und Effizienzplan</b><br>und unterstützen bei Bewilligungen und Fördergeldern – bis zur Umsetzung<br>und Abnahme.</p>

  <div class="steps">
    <p class="steps__title">So läuft die Zusammenarbeit</p>
    <ol>
      <li><b>1.</b> Erstkontakt (Telefon/E-Mail)</li>
      <li><b>2.</b> Analyse / Check vor Ort (Daten, Bedarf, Potenziale)</li>
      <li><b>3.</b> Konzept, Wirtschaftlichkeit &amp; Massnahmenplan</li>
      <li><b>4.</b> Umsetzung mit eingespieltem Partnernetzwerk</li>
      <li><b>5.</b> Optional: Monitoring &amp; Wartung für dauerhaft hohe Leistung</li>
    </ol>
  </div>

  <div class="abs footer" style="left:37px;top:668px">
    <b>TK AG Luzern</b><br>Lindenweg 14, CH-6015 Luzern<br>T +41 41 000 12 34<br>E info@tkag.lu<br>Web: www.tkag.lu
  </div>
  <div class="abs footer" style="left:269px;top:668px">
    Mitglied der Firmengruppe<br>NVK Luzern AG -<br>Netzwerk I Kompetenz I Innovation
  </div>
  <div class="abs brand" style="left:269px;top:716px;font-size:16px;gap:8px">
    <span class="brand__mark" style="width:26px;height:26px"></span>TK AG Luzern
  </div>
</section>

</body>
</html>
```